Top Tier Window Cleaning In Cincinnati OH

We need a post card made forAlways Sparkling Window Cleaning, in Cincinnati, OH. we offer Window Cleaning, Pressure Washing, Gutter Cleaning.
Phone number is: 513-555-0147
Email is: Harborcrest6@mailvento.com
Website is: Harborcrestwc.com

Target Market(s)

Residential high end homeowners. $500,000 homes and more.

Industry/Entity Type

Window Cleaning

Colors

Designer to choose colors to be used in the design.

Requirements
Must have
• It must have an embedded QR code that I have to link them "to schedule a FREE quote"
Nice to have
• I would like to see designs with pictures of nice houses on the front. and some designs with my logo and information

```html
<!DOCTYPE html>
<html lang="en">
<head>
<meta charset="utf-8">
<title>Harbor Crest Window Cleaning – Postcard</title>
<link rel="stylesheet" href="https://fonts.googleapis.com/css2?family=Montserrat:wght@400;500;700;800;900&family=Roboto+Condensed:wght@400;700&display=swap">
<style>
:root{
  --board:#7f7f7f;
  --white:#ffffff;
  --blue:#0a76b4;
  --blue-deep:#0b5f98;
  --blue-text:#0e74b8;
  --blue-bright:#1ea0e6;
  --ink:#1f1f1f;
  --charcoal:#2a2a2a;
  --red:#b30f0f;
  --sky-top:#2f6fb5;
  --sky-low:#8fb2d8;
  --brick:#6d6a66;
}
*{box-sizing:border-box;margin:0;padding:0}
html,body{width:1053px;height:1200px;overflow:hidden}
body{background:var(--board);font-family:"Montserrat",sans-serif;position:relative;color:var(--ink)}
.card{position:absolute;left:75px;width:902px;height:491px;background:var(--white);overflow:hidden;box-shadow:0 2px 6px rgba(0,0,0,.25)}
.card--front{top:82px}
.card--back{top:623px}
.abs{position:absolute}

/* front */
.brand-mark{left:187px;top:30px;width:54px;height:54px;border-radius:50%;background:var(--blue-text)}
.brand-heading{left:0;width:427px;top:160px;text-align:center;color:var(--blue-text);font-weight:800;line-height:1}
.brand-heading .line-1{display:block;font-size:29px;letter-spacing:.3px;color:var(--ink)}
.brand-heading .line-2{display:block;font-size:55px;margin-top:6px;letter-spacing:1px}
.brand-heading .line-3{display:block;font-size:55px;margin-top:2px;letter-spacing:1px}
.offer-bar{left:177px;top:327px;width:223px;height:61px;background:var(--charcoal);border-radius:0 10px 0 0}
.offer-text{left:212px;top:336px;color:var(--white);line-height:1}
.offer-text .first{font-size:23px;font-weight:400;letter-spacing:.3px}
.offer-text .first b{font-weight:800}
.offer-text .sub{display:block;font-size:13.5px;font-weight:800;color:var(--blue-bright);margin-top:4px;letter-spacing:.2px}
.offer-burst{left:67px;top:305px;width:126px;height:94px}
.offer-percent{left:83px;top:334px;color:var(--white);font-weight:900;font-size:48px;letter-spacing:-2px;line-height:1;font-family:"Roboto Condensed",sans-serif}
.offer-percent small{font-size:26px;letter-spacing:0}
.offer-off{left:150px;top:369px;color:var(--white);font-weight:800;font-size:11px}

.hero{left:427px;top:0;width:475px;height:398px;background:var(--blue);overflow:hidden}
.hero-art{left:0;top:0;width:475px;height:398px}
.service-label{color:var(--white);font-weight:800;font-size:16.5px;line-height:1.25;text-align:center;letter-spacing:.4px}
.icon-dot{width:56px;height:56px;border-radius:50%;background:var(--white);border:3px solid var(--blue-deep);display:flex;align-items:center;justify-content:center}
.icon-dot svg{width:30px;height:30px}

.quote-panel{left:0;top:398px;width:281px;height:93px;background:var(--blue)}
.quote-copy{left:65px;font-size:13px;font-weight:500;line-height:1.15}
.quote-copy strong{display:block;font-size:20px;font-weight:800;margin-top:5px;letter-spacing:.2px}
.card--front .quote-copy{top:412px;color:var(--white)}
.card--front .quote-copy strong{color:var(--charcoal)}
.phone{left:294px;font-size:29px;font-weight:700;letter-spacing:-.3px;display:flex;align-items:center;gap:6px;color:var(--ink)}
.phone svg{width:20px;height:20px}
.contact-list{left:530px;font-size:16.5px;line-height:1.22;color:var(--ink)}
.contact-list li{list-style:none;display:flex;align-items:center;gap:10px}
.contact-list svg{width:16px;height:16px;flex:none}

/* back */
.back-mark{left:57px;top:38px;display:flex;align-items:center;gap:10px;color:var(--blue-text);font-weight:800;font-size:20px}
.back-mark .dot{width:44px;height:44px;border-radius:50%;background:var(--blue-text)}
.qr-slot{left:650px;top:30px;width:86px;height:86px;border:2px solid var(--ink);background:var(--white)}
.postage{left:768px;top:37px;width:82px;height:69px;border:1.5px solid var(--ink);font-family:"Roboto Condensed",sans-serif;font-size:10px;text-align:center;line-height:1.25;padding-top:3px}
.postage b{font-size:12px}
.services-panel{left:0;top:153px;width:533px;height:263px;background:var(--blue)}
.services-title{left:41px;top:183px;color:var(--white);font-weight:800;font-size:30px;letter-spacing:1px}
.service-col{top:272px;height:141px;background:var(--blue-deep)}
.service-photo{top:232px;height:106px;border:2px solid var(--white);background:linear-gradient(180deg,#8fb5d9,#d6dadc 55%,#6f7a70)}
.service-name{top:365px;color:var(--white);font-weight:800;font-size:19.5px;line-height:1.05;text-align:center;letter-spacing:.3px}
.pointer{left:533px;top:268px;width:0;height:0;border-top:8px solid transparent;border-bottom:8px solid transparent;border-left:12px solid var(--blue)}
.promise-panel{left:533px;top:153px;width:369px;height:263px;background:var(--charcoal)}
.promise{left:626px;color:var(--white);font-weight:800;font-size:18.5px;line-height:1.08;letter-spacing:.3px}
.promise-icon{left:564px;width:44px;height:44px}
.card--back .quote-panel{top:416px;height:75px;background:var(--charcoal)}
.card--back .quote-copy{top:428px;color:var(--white)}
.card--back .quote-copy strong{color:var(--white);margin-top:4px}
</style>
</head>
<body>

<section class="card card--front" aria-label="Postcard front">
  <div class="abs brand-mark" aria-hidden="true"></div>
  <h1 class="abs brand-heading">
    <span class="line-1">HARBOR CREST</span>
    <span class="line-2">WINDOW</span>
    <span class="line-3">CLEANING</span>
  </h1>

  <div class="abs offer-bar"></div>
  <p class="abs offer-text"><span class="first">YOUR <b>FIRST</b></span><span class="sub">WINDOW CLEANING</span></p>
  <svg class="abs offer-burst" viewBox="0 0 126 94" aria-hidden="true">
    <polygon fill="var(--red)" points="63,0 71,6 80,2 86,10 96,8 99,17 109,18 109,27 118,31 114,40 122,47 114,54 118,63 109,67 109,76 99,77 96,86 86,84 80,92 71,88 63,94 55,88 46,92 40,84 30,86 27,77 17,76 17,67 8,63 12,54 4,47 12,40 8,31 17,27 17,18 27,17 30,8 40,10 46,2 55,6"/>
  </svg>
  <p class="abs offer-percent">50<small>%</small></p>
  <p class="abs offer-off">OFF</p>

  <div class="abs hero">
    <svg class="abs hero-art" viewBox="0 0 475 398">
      <defs>
        <linearGradient id="heroSky" x1="0" y1="0" x2="0" y2="1">
          <stop offset="0" stop-color="var(--sky-top)"/>
          <stop offset=".35" stop-color="var(--sky-low)"/>
          <stop offset=".62" stop-color="var(--brick)"/>
          <stop offset="1" stop-color="#4a4a42"/>
        </linearGradient>
      </defs>
      <g role="img" aria-label="Photograph of a two-storey brick family home with shuttered windows under a blue sky">
        <circle cx="238" cy="330" r="209" fill="url(#heroSky)"/>
        <rect x="0" y="280" width="475" height="118" fill="#5b5a52"/>
      </g>
      <path d="M31.2 300 A209 209 0 0 1 444.8 300" fill="none" stroke="rgba(255,255,255,.85)" stroke-width="6" aria-hidden="true"/>
    </svg>
    <p class="abs service-label" style="left:33px;top:84px;width:120px">WINDOW<br>CLEANING</p>
    <p class="abs service-label" style="left:181px;top:43px;width:124px">PRESSURE<br>WASHING</p>
    <p class="abs service-label" style="left:325px;top:84px;width:120px">GUTTER<br>CLEANING</p>
    <div class="abs icon-dot" style="left:70px;top:147px" aria-hidden="true">
      <svg viewBox="0 0 30 30"><rect x="5" y="5" width="20" height="20" fill="none" stroke="var(--blue-deep)" stroke-width="2"/><path d="M15 5v20M5 15h20" stroke="var(--blue-deep)" stroke-width="1.6"/></svg>
    </div>
    <div class="abs icon-dot" style="left:216px;top:93px" aria-hidden="true">
      <svg viewBox="0 0 30 30"><path d="M6 15l9-8 9 8v9H6z" fill="none" stroke="var(--blue-deep)" stroke-width="2"/><path d="M11 24v-5h8v5" fill="none" stroke="var(--blue-deep)" stroke-width="1.6"/></svg>
    </div>
    <div class="abs icon-dot" style="left:350px;top:145px" aria-hidden="true">
      <svg viewBox="0 0 30 30"><path d="M5 9h20l-2 5H7z" fill="none" stroke="var(--blue-deep)" stroke-width="2"/><path d="M19 14v10" stroke="var(--blue-deep)" stroke-width="2"/></svg>
    </div>
  </div>

  <div class="abs quote-panel"></div>
  <p class="abs quote-copy">Need a free quote to clean<br>your home or business?<strong>CALL US TODAY</strong></p>

  <p class="abs phone" style="top:423px">
    <svg viewBox="0 0 24 24" aria-hidden="true"><path fill="var(--blue-text)" d="M6.6 10.8a15.1 15.1 0 0 0 6.6 6.6l2.2-2.2c.3-.3.7-.4 1-.2 1.1.4 2.3.6 3.6.6.6 0 1 .4 1 1V20c0 .6-.4 1-1 1A17 17 0 0 1 3 4c0-.6.4-1 1-1h3.5c.6 0 1 .4 1 1 0 1.3.2 2.5.6 3.6.1.3 0 .7-.2 1z"/></svg>
    513-555-0147
  </p>
  <ul class="abs contact-list" style="top:424px">
    <li><svg viewBox="0 0 16 16" aria-hidden="true"><rect x="1" y="3" width="14" height="10" rx="1" fill="var(--blue-text)"/><path d="M1 4l7 5 7-5" stroke="#fff" fill="none" stroke-width="1.3"/></svg>Harborcrest6@mailvento.com</li>
    <li><svg viewBox="0 0 16 16" aria-hidden="true"><circle cx="8" cy="8" r="7" fill="none" stroke="var(--blue-text)" stroke-width="1.6"/><path d="M1 8h14M8 1c-3 3-3 11 0 14M8 1c3 3 3 11 0 14" stroke="var(--blue-text)" fill="none" stroke-width="1.2"/></svg>www.harborcrestwc.com</li>
  </ul>
</section>

<section class="card card--back" aria-label="Postcard back">
  <div class="abs back-mark"><span class="dot" aria-hidden="true"></span>Harbor Crest Window Cleaning</div>
  <div class="abs qr-slot" role="img" aria-label="QR code linking to schedule a free quote"></div>
  <div class="abs postage">PRST STD<br>ECRWSS<br>U.S. POSTAGE<br><b>PAID</b><br>EDDM Retail</div>

  <div class="abs services-panel"></div>
  <h2 class="abs services-title">OUR SERVICES</h2>

  <div class="abs service-col" style="left:37px;width:164px"></div>
  <div class="abs service-col" style="left:201px;width:148px;background:var(--blue)"></div>
  <div class="abs service-col" style="left:349px;width:152px"></div>
  <div class="abs service-photo" style="left:51px;width:138px" role="img" aria-label="Photograph of clean multi-pane sash windows"></div>
  <div class="abs service-photo" style="left:208px;width:137px" role="img" aria-label="Photograph of a freshly pressure-washed white sided house"></div>
  <div class="abs service-photo" style="left:357px;width:137px" role="img" aria-label="Photograph of a shingled roof with cleared gutters"></div>
  <p class="abs service-name" style="left:37px;width:164px">WINDOW<br>CLEANING</p>
  <p class="abs service-name" style="left:201px;width:148px">PRESSURE<br>WASHING</p>
  <p class="abs service-name" style="left:349px;width:152px">GUTTER<br>CLEANING</p>

  <div class="abs promise-panel"></div>
  <div class="abs pointer" aria-hidden="true"></div>
  <svg class="abs promise-icon" style="top:186px" viewBox="0 0 44 44" aria-hidden="true"><circle cx="22" cy="22" r="20" fill="none" stroke="var(--blue-bright)" stroke-width="2"/><circle cx="22" cy="22" r="15" fill="none" stroke="var(--blue-bright)" stroke-width="1.5"/><polygon points="22,12 25,19 32,19.5 26.5,24 28.5,31 22,27 15.5,31 17.5,24 12,19.5 19,19" fill="none" stroke="var(--blue-bright)" stroke-width="1.5"/></svg>
  <p class="abs promise" style="top:198px">5-STAR CUSTOMER<br>EXPERIENCE</p>
  <svg class="abs promise-icon" style="top:263px" viewBox="0 0 44 44" aria-hidden="true"><circle cx="22" cy="22" r="19" fill="none" stroke="var(--blue-bright)" stroke-width="2"/><path d="M10 14c6 2 8 8 4 12s2 8 6 10M26 4c-2 6 4 8 8 8M24 40c0-6 6-8 6-14" fill="none" stroke="var(--blue-bright)" stroke-width="1.6"/></svg>
  <p class="abs promise" style="top:273px">ECO-FRIENDLY<br>PRACTICES</p>
  <svg class="abs promise-icon" style="top:338px;left:566px" viewBox="0 0 44 44" aria-hidden="true"><rect x="3" y="8" width="32" height="32" fill="none" stroke="var(--blue-bright)" stroke-width="2.4"/><path d="M11 22l8 8L42 4" fill="none" stroke="var(--blue-bright)" stroke-width="2.6"/></svg>
  <p class="abs promise" style="top:348px">100% SATISFACTION<br>GUARANTEE</p>

  <div class="abs quote-panel"></div>
  <p class="abs quote-copy">Need a free quote to clean<br>your home or business?<strong>CALL US TODAY</strong></p>

  <p class="abs phone" style="top:433px">
    <svg viewBox="0 0 24 24" aria-hidden="true"><path fill="var(--blue-text)" d="M6.6 10.8a15.1 15.1 0 0 0 6.6 6.6l2.2-2.2c.3-.3.7-.4 1-.2 1.1.4 2.3.6 3.6.6.6 0 1 .4 1 1V20c0 .6-.4 1-1 1A17 17 0 0 1 3 4c0-.6.4-1 1-1h3.5c.6 0 1 .4 1 1 0 1.3.2 2.5.6 3.6.1.3 0 .7-.2 1z"/></svg>
    513-555-0147
  </p>
  <ul class="abs contact-list" style="top:434px">
    <li><svg viewBox="0 0 16 16" aria-hidden="true"><rect x="1" y="3" width="14" height="10" rx="1" fill="var(--blue-text)"/><path d="M1 4l7 5 7-5" stroke="#fff" fill="none" stroke-width="1.3"/></svg>Harborcrest6@mailvento.com</li>
    <li><svg viewBox="0 0 16 16" aria-hidden="true"><circle cx="8" cy="8" r="7" fill="none" stroke="var(--blue-text)" stroke-width="1.6"/><path d="M1 8h14M8 1c-3 3-3 11 0 14M8 1c3 3 3 11 0 14" stroke="var(--blue-text)" fill="none" stroke-width="1.2"/></svg>www.harborcrestwc.com</li>
  </ul>
</section>

</body>
</html>
```